Wanderlark Gin - Bottle Label for a craft Gin about to be launched on the world from New Zealand

We are a start up craft distillery in New Zealand. We have developed a wonderful Gin using our own grain spirit and both traditional and New Zealand native botanicals (Manuka to be specific), chosen our bottle and the name "Wanderlark" and done a bit of amateur label design and now we are looking for someone to make it great.

Feel free to change up our amateur concept but give us something that will pop from the back bar and scream authenticity, craft and individuality.

The attached files give you the specifications of the bottle, our current concept for a Wanderlark label and an earlier concept drawing that gives an idea of where we are thinking the two labels should go on the front of the bottle.

Thanks, we look forward to your ideas!!

Target Market(s)

High end and craft Gin drinkers. Hipsters and cocktail barflys and their bar tenders and bar owners

Requirements
Must have
• Attractive individuality
Nice to have
• Coolness
Should not have
• Uncoolness

```html
<!DOCTYPE html>
<html lang="en">
<head>
<meta charset="utf-8">
<title>Wanderlark Gin – Label Artwork</title>
<link href="https://fonts.googleapis.com/css2?family=Antonio:wght@300;400;700&display=swap" rel="stylesheet">
<style>
  :root {
    --orange: #f26c23;
    --orange-soft: #f6a57a;
    --ink: #231f20;
    --white: #ffffff;
    --cut-line: #9a9a9a;
  }
  html, body {
    margin: 0;
    padding: 0;
    width: 1200px;
    height: 860px;
    overflow: hidden;
    background: var(--white);
  }
  .board {
    position: relative;
    width: 1200px;
    height: 860px;
    font-family: "Antonio", "Arial Narrow", sans-serif;
    color: var(--ink);
  }
  .material-note {
    position: absolute;
    left: 86px;
    top: 52px;
    margin: 0;
    font-size: 13px;
    font-weight: 300;
    letter-spacing: -0.2px;
  }

  /* Neck label */
  .neck-label {
    position: absolute;
    left: 84px;
    top: 80px;
    width: 532px;
    height: 120px;
    background: var(--orange);
    border: 1px dashed var(--cut-line);
    box-sizing: border-box;
    text-align: center;
  }
  .neck-label .origin {
    position: absolute;
    left: 0;
    right: 0;
    top: 34px;
    margin: 0;
    font-size: 12.5px;
    font-weight: 300;
    line-height: 16px;
    color: var(--white);
  }
  .neck-label .brand-name {
    position: absolute;
    left: 0;
    right: 0;
    top: 80px;
    margin: 0;
    font-size: 26px;
    font-weight: 700;
    line-height: 28px;
    letter-spacing: -0.5px;
    white-space: nowrap;
    color: var(--ink);
  }

  /* Front label */
  .front-label {
    position: absolute;
    left: 97px;
    top: 222px;
    width: 237px;
    height: 577px;
    border: 1px dashed var(--cut-line);
    box-sizing: border-box;
    overflow: hidden;
  }
  .front-label .dots {
    position: absolute;
    left: 85px;
    top: 12px;
  }
  .front-label .origin {
    position: absolute;
    left: 83px;
    top: 116px;
    margin: 0;
    font-size: 17px;
    font-weight: 300;
    line-height: 23px;
  }
  .front-label .brand-mark {
    position: absolute;
    left: 22px;
    top: 192px;
  }
  .front-label .brand-name {
    position: absolute;
    left: 0;
    right: 0;
    top: 390px;
    margin: 0;
    text-align: center;
    font-size: 45px;
    font-weight: 700;
    line-height: 66px;
    letter-spacing: -1px;
    white-space: nowrap;
  }
  .front-label .volume-badge {
    position: absolute;
    left: 63px;
    top: 462px;
  }
  .front-label .volume-text {
    position: absolute;
    left: 83px;
    top: 479px;
    margin: 0;
    font-size: 13px;
    font-weight: 300;
    line-height: 17px;
    color: var(--white);
  }

  /* Back label */
  .back-label {
    position: absolute;
    left: 361px;
    top: 323px;
    width: 208px;
    height: 267px;
    border: 1px dashed var(--cut-line);
    box-sizing: border-box;
  }
  .back-label .recipe-panel {
    position: absolute;
    left: 11px;
    top: 11px;
    width: 184px;
    height: 244px;
    background: var(--orange);
    color: var(--white);
    text-align: center;
  }
  .back-label .recipe-title {
    margin: 36px 0 2px;
    font-size: 32px;
    font-weight: 300;
    line-height: 36px;
  }
  .back-label .recipe-notes,
  .back-label .serve {
    margin: 0;
    font-size: 14px;
    font-weight: 300;
    line-height: 20px;
    letter-spacing: -0.2px;
    white-space: nowrap;
  }
  .back-label .serve {
    margin-top: 20px;
  }
</style>
</head>
<body>
<main class="board">
  <p class="material-note">using CLEAR on CLEAR sticker label material</p>

  <section class="neck-label" aria-label="Neck label">
    <p class="origin">NEW ZEALAND<br>EXTRA ORDINARY<br>GIN</p>
    <p class="brand-name">WANDERLARK</p>
  </section>

  <section class="front-label" aria-label="Front label">
    <svg class="dots" width="12" height="92" viewBox="0 0 12 92" aria-hidden="true">
      <circle cx="6" cy="6" r="4.2" fill="var(--orange-soft)"/>
      <circle cx="6" cy="27" r="4.2" fill="var(--orange-soft)"/>
      <circle cx="6" cy="48" r="4.2" fill="var(--orange-soft)"/>
      <circle cx="6" cy="68" r="4.2" fill="var(--orange-soft)"/>
      <circle cx="6" cy="86" r="4.2" fill="var(--orange-soft)"/>
    </svg>
    <p class="origin">NEW ZEALAND<br>EXTRA ORDINARY<br>GIN</p>
    <svg class="brand-mark" width="196" height="196" viewBox="0 0 196 196" aria-hidden="true">
      <circle cx="98" cy="98" r="96" fill="var(--orange)"/>
    </svg>
    <p class="brand-name">WANDERLARK</p>
    <svg class="volume-badge" width="110" height="90" viewBox="0 0 110 90" aria-hidden="true">
      <ellipse cx="55" cy="45" rx="54" ry="44" fill="var(--orange)"/>
    </svg>
    <p class="volume-text">500 ML.<br>84 PROOF<br>42% ALC. BY VOL.</p>
  </section>

  <section class="back-label" aria-label="Back label">
    <div class="recipe-panel">
      <h2 class="recipe-title">RECIPE #3</h2>
      <p class="recipe-notes">A CLASSICALY INSPIRED GIN<br>WITH DEVELOPED CITRUS NOTES<br>FROM THE MANUKA<br>BERRIES FROM ROWAN’S MATES.</p>
      <p class="serve">BEST WITH AN EQUAL MIX<br>OF SOME FANCY TONIC</p>
    </div>
  </section>
</main>
</body>
</html>
```